Pondmentor: an app for coaches and students in golf and fitness

I currently have an app that is called Pondmentor and I am redoing the app completely and with this I am looking for a cool design for the app. I am not happy with the design as it is at the moment. The app should have a nice welcome and when you are logged in the dashboard must be very modern. It is a golf app that have 2 type of users. 1 user is the coach and the other user is the student. Those users can see different things of course.
The coach is normally paying a subscription charge for using the app but I want to get the students to pay for different tools that I will be offering via the app. To me the dashboard and the homepage of the app (once you have downloaded the app) is important. Here I would like to get the student as well as the coach the feeling of what the app can offer. The app offers features like Calendar (here the student can book the coach via the calendar), Chat (here the coach and the student can chat with each other as well as the coach can creat group chats with several students), Notes (here the coach as well as the student can create notes for their lessons), video tips (here the coach can upload video tips for his/her students, online lesson (the student can take online lessons by uploading recorded videos..and so on

Target Market(s)

Sport coaches (for start it will be mostly golf coaches)

Industry/Entity Type

Sports

Font styles to use
Sans Serif

Colors
0054AA
0677BA
7BADD7
CADEEF
E8F1F8

Requirements
Must have
• modern design and easy navigation.
Nice to have
• It all starts with the dashboard
Should not have
• boring standard style.

```html
<!DOCTYPE html>
<html lang="en">
<head>
<meta charset="utf-8">
<title>Pondmentor app screens</title>
<link href="https://fonts.googleapis.com/css2?family=Nunito+Sans:wght@400;600;700;800&family=Fira+Sans+Condensed:wght@400;600;700&display=swap" rel="stylesheet">
<style>
:root{
  --page:#eeeeec;
  --white:#ffffff;
  --ink:#0c1a20;
  --sky:#87d3f0;
  --deep:#0e5e78;
  --teal:#1d6e78;
  --menu-blue:#139bc0;
  --menu-soft:#2fb3d8;
  --menu-text:#0c6a8a;
  --grey:#6d7478;
}
*{box-sizing:border-box;margin:0;padding:0}
html,body{width:1200px;height:626px;overflow:hidden;background:var(--page);font-family:"Nunito Sans",sans-serif}
.screen{position:absolute;top:78px;width:199px;height:430px;border-radius:22px;overflow:hidden}
.abs{position:absolute}
.center{left:0;right:0;text-align:center}
.status{left:0;right:0;top:0;height:23px;background:#000;color:var(--white);font-size:8px;font-weight:700}
.status .time{position:absolute;left:15px;top:7px}
.status svg{position:absolute;right:14px;top:8px}
.home-bar{left:64px;width:71px;top:424px;height:2px;border-radius:2px}
.wordmark{font-weight:800;letter-spacing:-.3px;white-space:nowrap;display:flex;align-items:center;gap:3px}
.wordmark .dot{border-radius:50%;background:var(--sky);flex:none}

/* splash */
.splash{left:106px;background:var(--white)}
.splash .wordmark{left:0;right:0;top:196px;justify-content:center;font-size:28px;color:var(--deep)}
.splash .wordmark .dot{width:16px;height:16px}

/* welcome */
.welcome{left:374px}
.welcome .photo{left:0;top:23px;right:0;bottom:0;background:linear-gradient(180deg,#2f8a86 0%,#4c9f7a 45%,#5eae64 80%,#6cb85a 100%)}
.welcome .wordmark{left:0;right:0;top:78px;justify-content:center;font-size:19px;color:var(--white)}
.welcome .wordmark .dot{width:11px;height:11px}
.hero{font-family:"Fira Sans Condensed",sans-serif;color:var(--white)}
.hero-small{top:180px;font-size:15px;font-weight:600}
.hero-big{top:199px;font-size:27px;font-weight:700}
.hero-sub{top:245px;font-size:12.5px;line-height:12px;font-weight:600}
.btn{left:32px;width:135px;height:24px;border-radius:12px;font-family:"Fira Sans Condensed",sans-serif;font-size:8px;font-weight:600;display:flex;align-items:center;justify-content:center}
.btn-login{top:350px;background:var(--sky);color:var(--deep)}
.btn-register{top:381px;background:var(--deep);color:var(--white)}

/* dashboard */
.dashboard{left:642px}
.dash-bg{left:0;top:23px;right:0;bottom:0;background:linear-gradient(180deg,#1c6a78 0%,#1f7177 40%,#2b8266 75%,#3f9a4a 100%)}
.dash-header{left:0;top:23px;right:0;height:76px;background:linear-gradient(180deg,#3c8c70,#2d7a72)}
.menu-btn{left:17px;top:35px;width:20px;height:21px;border-radius:3px;background:rgba(255,255,255,.25)}
.menu-btn i{position:absolute;left:5px;width:10px;height:1.2px;background:var(--white)}
.dashboard .wordmark{left:108px;top:40px;font-size:12px;color:var(--white)}
.dashboard .wordmark .dot{width:7px;height:7px}
.dash-title{top:76px;font-size:11px;font-weight:700;color:var(--white);letter-spacing:.3px}
.greeting{top:110px;font-size:6.5px;font-weight:800;color:var(--white)}
.tasks-title{top:139px;font-size:8px;color:var(--white)}
.task-card{left:8px;width:183px;top:154px;height:62px;border-radius:8px;background:var(--white);color:var(--grey)}
.task-card .label{left:7px;top:15px;font-size:6px}
.task-card .hours{right:7px;top:15px;font-size:6px}
.task-card .rule{left:7px;right:7px;top:31px;height:1px;background:#d7dcdf}
.task-card .students{left:7px;top:36px;font-size:6px;font-weight:700}
.task-card .names{left:42px;top:37px;display:grid;grid-template-columns:repeat(3,36px);row-gap:3px;font-size:4.5px}
.tile{border-radius:8px;background:rgba(255,255,255,.16);border:1px solid rgba(255,255,255,.35);color:var(--white)}
.tile-products{left:8px;top:225px;width:87px;height:62px}
.tile-calendar{left:104px;top:225px;width:87px;height:62px}
.tile h3{position:absolute;top:5px;left:0;right:0;text-align:center;font-size:8px;font-weight:700;letter-spacing:.2px}
.tile-products .desc{left:6px;top:25px;font-size:6.3px;font-weight:700;line-height:7px}
.tile-products .more{left:6px;top:49px;font-size:6.3px}
.day{left:15px;top:15px;font-size:27px;font-weight:800;line-height:28px;letter-spacing:-1px}
.date-meta{left:51px;top:18px;font-size:7.5px;line-height:8.5px}
.date-meta b{font-weight:800}
.tile-calendar .more{left:0;right:0;top:49px;text-align:center;font-size:6.3px}
.tile-video{left:8px;top:296px;width:183px;height:61px}
.tile-video h3{left:15px;right:auto;text-align:left}
.thumb{top:22px;width:51px;height:31px;border-radius:4px;border:1px solid rgba(255,255,255,.7)}
.thumb svg{position:absolute;left:19px;top:9px}
.dots{left:0;right:0;top:373px;display:flex;justify-content:center;gap:7px}
.dots i{width:4px;height:4px;border-radius:50%;background:var(--white)}

/* menu */
.menu-screen{left:898px;background:var(--menu-blue)}
.menu-screen .wordmark{left:15px;top:40px;font-size:12px;color:var(--white)}
.menu-screen .wordmark .dot{width:7px;height:7px}
.menu-list{left:15px;top:90px;width:84px;list-style:none}
.menu-list li{height:17px;margin-bottom:5.5px;background:var(--white);color:var(--menu-text);font-size:8px;padding-left:7px;display:flex;align-items:center}
.menu-list li.active{background:var(--deep);color:var(--white)}
.menu-foot{left:15px;width:84px;height:17px;background:var(--menu-soft);color:#dff4fb;font-size:6.5px;padding-left:7px;display:flex;align-items:center}
.peek{left:148px;top:67px;width:51px;height:331px;overflow:hidden;background:linear-gradient(180deg,#1c6a78 0%,#1f7177 45%,#2b8266 80%,#3f9a4a 100%)}
.peek-header{left:0;top:0;width:100%;height:62px;background:linear-gradient(180deg,#3c8c70,#2d7a72)}
.peek-card{left:6px;width:60px;border-radius:7px}
</style>
</head>
<body>

<section class="screen splash" aria-label="Splash screen">
  <div class="abs wordmark"><span class="dot"></span>pondmentor</div>
  <div class="abs home-bar" style="background:var(--ink)"></div>
</section>

<section class="screen welcome" aria-label="Welcome screen">
  <div class="abs photo" role="img" aria-label="Golfer mid-swing on a green fairway with forested hills, tinted teal"></div>
  <div class="abs status"><span class="time">13:18</span>
    <svg width="34" height="7" viewBox="0 0 34 7"><rect x="0" y="5" width="1.5" height="2" fill="#777"/><rect x="2.5" y="3.5" width="1.5" height="3.5" fill="#777"/><rect x="5" y="2" width="1.5" height="5" fill="#777"/><path d="M11 3.5a4 4 0 0 1 6 0M12.3 5a2 2 0 0 1 3.4 0" stroke="#777" fill="none" stroke-width="1"/><rect x="22" y="1" width="10" height="5.5" rx="1" fill="#777"/></svg>
  </div>
  <div class="abs wordmark"><span class="dot"></span>pondmentor</div>
  <p class="abs center hero hero-small">You are a</p>
  <p class="abs center hero hero-big">golf player</p>
  <p class="abs center hero hero-sub">Motivation Is The First Step<br>To Success</p>
  <div class="abs btn btn-login">Log In</div>
  <div class="abs btn btn-register">Registration</div>
  <div class="abs home-bar" style="background:var(--ink)"></div>
</section>

<section class="screen dashboard" aria-label="Coach dashboard">
  <div class="abs dash-bg" role="img" aria-label="Grass field with a golf club and ball, fading up into teal"></div>
  <div class="abs dash-header" role="img" aria-label="Golfer swinging on a course, tinted green"></div>
  <div class="abs status"><span class="time">13:18</span>
    <svg width="34" height="7" viewBox="0 0 34 7"><rect x="0" y="5" width="1.5" height="2" fill="#fff"/><rect x="2.5" y="3.5" width="1.5" height="3.5" fill="#fff"/><rect x="5" y="2" width="1.5" height="5" fill="#fff"/><path d="M11 3.5a4 4 0 0 1 6 0M12.3 5a2 2 0 0 1 3.4 0" stroke="#fff" fill="none" stroke-width="1"/><rect x="22" y="1" width="10" height="5.5" rx="1" fill="#fff"/></svg>
  </div>
  <div class="abs menu-btn"><i style="top:7px"></i><i style="top:10px"></i><i style="top:13px"></i></div>
  <div class="abs wordmark"><span class="dot"></span>pondmentor</div>
  <h1 class="abs center dash-title">MY DASHBOARD</h1>
  <p class="abs center greeting">Wecome, Coach Elliot!</p>
  <p class="abs center tasks-title">Today you have such tasks:</p>
  <div class="abs task-card">
    <span class="abs label">Group lesson</span>
    <span class="abs hours">1pm - 4 pm</span>
    <div class="abs rule"></div>
    <span class="abs students">Students:</span>
    <div class="abs names"><span>Lorem Ipsum</span><span>Lorem Ipsum</span><span>Lorem Ipsum</span><span>Lorem Ipsum</span><span>Lorem Ipsum</span><span>Lorem Ipsum</span></div>
  </div>
  <div class="abs tile tile-products">
    <h3>MY PRODUCTS</h3>
    <p class="abs desc">Book and manage your<br>appointments 24/7</p>
    <p class="abs more">Watch Your Events Now</p>
  </div>
  <div class="abs tile tile-calendar">
    <h3>MY CALENDAR</h3>
    <span class="abs day">21</span>
    <p class="abs date-meta">WEN<br><b>APR</b><br>2022</p>
    <p class="abs more">Watch events</p>
  </div>
  <div class="abs tile tile-video">
    <h3>VIDEO TIPS</h3>
    <div class="abs thumb" style="left:7px;background:linear-gradient(135deg,#8fa39a,#5f8a5c)" role="img" aria-label="Video tip: coach adjusting grip"><svg width="10" height="10" viewBox="0 0 10 10"><path d="M2 1l7 4-7 4z" fill="#fff"/></svg></div>
    <div class="abs thumb" style="left:66px;background:linear-gradient(135deg,#7fa86a,#a9c08a)" role="img" aria-label="Video tip: player holding a club on the course"><svg width="10" height="10" viewBox="0 0 10 10"><path d="M2 1l7 4-7 4z" fill="#fff"/></svg></div>
    <div class="abs thumb" style="left:124px;background:linear-gradient(180deg,#5c8a6a,#7fae6a)" role="img" aria-label="Video tip: golfer finishing a swing"></div>
  </div>
  <div class="abs dots"><i></i><i></i><i></i></div>
  <div class="abs home-bar" style="background:var(--white)"></div>
</section>

<section class="screen menu-screen" aria-label="Navigation menu">
  <div class="abs status"><span class="time">13:18</span>
    <svg width="34" height="7" viewBox="0 0 34 7"><rect x="0" y="5" width="1.5" height="2" fill="#fff"/><rect x="2.5" y="3.5" width="1.5" height="3.5" fill="#fff"/><rect x="5" y="2" width="1.5" height="5" fill="#fff"/><path d="M11 3.5a4 4 0 0 1 6 0M12.3 5a2 2 0 0 1 3.4 0" stroke="#fff" fill="none" stroke-width="1"/><rect x="22" y="1" width="10" height="5.5" rx="1" fill="#fff"/></svg>
  </div>
  <div class="abs wordmark"><span class="dot"></span>pondmentor</div>
  <ul class="abs menu-list">
    <li>Calendar</li><li>Online lessons</li><li>My products</li><li>My students</li>
    <li>Video Editor</li><li>Chat</li><li>Video Tips</li><li class="active">Pond365</li>
  </ul>
  <div class="abs menu-foot" style="top:358px">My Account</div>
  <div class="abs menu-foot" style="top:382px">Languages</div>
  <div class="abs peek" role="img" aria-label="Dashboard sliding out behind the menu">
    <div class="abs peek-header"></div>
    <span class="abs" style="left:46px;top:44px;color:#fff;font-size:9px;font-weight:700">M</span>
    <span class="abs" style="left:40px;top:95px;color:#fff;font-size:6.5px">Tod</span>
    <div class="abs peek-card" style="top:107px;height:50px;background:#fff;color:var(--grey);font-size:5px;padding:12px 0 0 6px">Group lesson<br><br><b>Students:</b> Lorem</div>
    <div class="abs peek-card tile" style="top:163px;height:51px;color:#fff;font-size:5px;padding:5px 0 0 6px"><b style="font-size:6.5px;padding-left:7px">MY PRODU</b><br><br><b>Book and mana<br>appointments 2</b><br><br>Watch Your Eve</div>
    <div class="abs peek-card tile" style="top:222px;height:50px;color:#fff;font-size:6.5px;font-weight:700;padding:4px 0 0 12px">VIDEO TIP</div>
    <div class="abs" style="left:12px;top:238px;width:40px;height:26px;border-radius:3px;background:linear-gradient(135deg,#8fa39a,#5f8a5c);border:1px solid rgba(255,255,255,.7)"></div>
  </div>
  <div class="abs home-bar" style="background:var(--white)"></div>
</section>

</body>
</html>
```